Property Management business needs Business cards designed

We provide a premium property management service based in Sydney's Norther Beaches. We want people to feel confident in choosing us to manage their investment properties. We offer a much more personalized service than other estate agents.
We want a modern clean design. Something that shows confidence without being complicated.
Logo attached.

Target Market(s)

35-70yo Male and Female with strong property portfolios within Sydney's Norther Beaches

Industry/Entity Type

Property Management

Contact Information for Business Card

Address: Suite 7, 12-14 Kelvin Parade, Harlow NSW 2188
Two separate named cards.
Tom Ardley - 0491 570 118 tom@harbourvaleestates.com.au
Clara Dunmore - 0491 570 263 clara@harbourvaleestates.com.au

Requirements
Must have
• Business logo, name, number, address, email.

```html
<!DOCTYPE html>
<html lang="en">
<head>
<meta charset="utf-8">
<title>Harbourvale Estates – Business Cards</title>
<link rel="stylesheet" href="https://fonts.googleapis.com/css2?family=Open+Sans:wght@400;600;700&display=swap">
<style>
  :root {
    --teal: #177b8b;
    --ink: #1b1b1b;
    --text: #3a3a3a;
    --card: #ffffff;
    --backdrop: #e7e4e0;
  }
  * { margin: 0; padding: 0; box-sizing: border-box; }
  html, body { width: 1200px; height: 900px; overflow: hidden; }
  body {
    position: relative;
    background: var(--backdrop);
    font-family: "Open Sans", Arial, sans-serif;
  }
  .card {
    position: absolute;
    background: var(--card);
    border-radius: 16px;
    overflow: hidden;
    box-shadow: 0 6px 18px rgba(0,0,0,0.12);
  }
  .card--front { left: 78px; top: 35px; width: 588px; height: 362px; }
  .card--back { left: 390px; top: 506px; width: 564px; height: 349px; }

  .front-band { position: absolute; left: 0; top: 27px; width: 588px; height: 103px; display: block; }

  .brand {
    position: absolute;
    display: flex;
    align-items: center;
    gap: 10px;
    color: var(--ink);
    font-weight: 700;
    white-space: nowrap;
    letter-spacing: 0.5px;
  }
  .brand__dot { border-radius: 50%; background: var(--teal); flex: none; }
  .card--front .brand { left: 290px; top: 78px; transform: translate(-50%, -50%); font-size: 22px; }
  .card--front .brand__dot { width: 14px; height: 14px; }
  .card--back .brand { left: 290px; top: 174px; transform: translate(-50%, -50%); font-size: 32px; }
  .card--back .brand__dot { width: 20px; height: 20px; }

  .contact { position: absolute; left: 0; top: 172px; width: 100%; text-align: center; color: var(--text); }
  .contact__name { color: var(--teal); font-weight: 600; font-size: 20px; line-height: 28px; }
  .contact__address { margin-top: 12px; font-size: 15px; line-height: 21px; }
  .contact__lines { margin-top: 18px; font-size: 15px; line-height: 21px; }
  .contact__line { display: flex; justify-content: center; align-items: center; gap: 8px; }
  .contact__icon { width: 12px; height: 12px; fill: var(--teal); flex: none; }

  .back-stripe { position: absolute; left: 39px; top: 0; width: 43px; height: 100%; background: var(--teal); }
</style>
</head>
<body>
  <section class="card card--front" aria-label="Business card front">
    <svg class="front-band" viewBox="0 0 588 103" aria-hidden="true">
      <rect x="0" y="0" width="588" height="103" fill="var(--teal)"/>
      <ellipse cx="290" cy="51.5" rx="150" ry="62" fill="#ffffff"/>
    </svg>
    <div class="brand"><span class="brand__dot"></span>HARBOURVALE ESTATES</div>

    <div class="contact">
      <p class="contact__name">Tom Ardley</p>
      <p class="contact__address">Suite 7, 12-14 Kelvin Parade<br>Harlow NSW 2188</p>
      <div class="contact__lines">
        <p class="contact__line">
          <svg class="contact__icon" viewBox="0 0 24 24" aria-hidden="true"><path d="M6.6 10.8a15.1 15.1 0 0 0 6.6 6.6l2.2-2.2a1 1 0 0 1 1-.25 11.4 11.4 0 0 0 3.6.57 1 1 0 0 1 1 1V20a1 1 0 0 1-1 1A17 17 0 0 1 3 4a1 1 0 0 1 1-1h3.5a1 1 0 0 1 1 1c0 1.25.2 2.45.57 3.57a1 1 0 0 1-.25 1z"/></svg>
          0491 570 118
        </p>
        <p class="contact__line">
          <svg class="contact__icon" viewBox="0 0 24 24" aria-hidden="true"><path d="M2 5h20v14H2z M2 5l10 8 10-8" fill="var(--teal)" stroke="#fff" stroke-width="1.5"/></svg>
          tom@harbourvaleestates.com.au
        </p>
      </div>
    </div>
  </section>

  <section class="card card--back" aria-label="Business card back">
    <div class="back-stripe"></div>
    <div class="brand"><span class="brand__dot"></span>HARBOURVALE ESTATES</div>
  </section>
</body>
</html>
```